ZEPRILO.COM is a premium domain sales company. Our competitors are companies like vastplots.example, getparcels.example, peerwords.example. Our current site is at www.zeprilos.example.

We want to have the ability to search for domains, to highlight special offers and have some testimonials on the index page.

The logo for the site is attached.

Please be sure that the order form fits on the screen without scrolling the page. I want the entire form, including the submit button to fit without any page scrolling.

Delivered product - INDEX PAGE, ORDER FORM AND CONTENT PAGE PSDs.

Target Market(s)

Small to Medium business professionals

Industry/Entity Type

It Company

Requirements
Must have
• 1. List of domains for sale
2. Simple search box with button to run the search
3. link for advanced search
4. testimonial area. Note - this can be a small box where a different testimonial is displayed on each page load.
Nice to have
• Would like the site to have some white space. Don't want a heavily packed website. Give it an "airy" feel.

```html
<!DOCTYPE html>
<html lang="en">
<head>
<meta charset="utf-8">
<title>ZEPRILO.COM – Premium Domains</title>
<link rel="stylesheet" href="https://fonts.googleapis.com/css2?family=Arimo:wght@400;700&family=Open+Sans:wght@400;600&display=swap">
<style>
:root{
  --blue-dark:#0b6fae;
  --blue-mid:#1d95d6;
  --blue-light:#3fb3ea;
  --navy:#1b3d6e;
  --green:#17742c;
  --green-logo:#1f7a34;
  --logo-blue:#17407c;
  --band-top:#d6e6bb;
  --band-bottom:#eef0ea;
  --page:#ececec;
  --row-hi:#e3ead7;
  --line:#dadada;
  --text:#222;
  --footer:#d2d2d2;
  --footer-text:#2a5e8c;
}
*{box-sizing:border-box;margin:0;padding:0}
html,body{width:1200px;height:961px;overflow:hidden}
body{position:relative;background:var(--page);font-family:"Arimo",Arial,sans-serif;color:var(--text)}
.abs{position:absolute}
.header{left:0;top:0;width:1200px;height:68px;background:linear-gradient(#fff,#f4f7f9)}
.logo{left:188px;top:14px;font-size:44px;font-weight:700;color:var(--logo-blue);letter-spacing:-1px;line-height:50px}
.nav a{position:absolute;top:27px;font-size:18px;color:#222;text-decoration:none}
.nav a.current{color:var(--navy);font-weight:700}
.nav .sep{position:absolute;top:26px;width:1px;height:24px;background:#aaa}
.hero{left:0;top:68px;width:1200px;height:354px;background:radial-gradient(ellipse 700px 400px at 330px 150px,var(--blue-light),var(--blue-mid) 55%,var(--blue-dark))}
.hero h1{left:177px;top:128px;font-size:33px;font-weight:400;color:var(--logo-blue)}
.hero .lead{left:177px;top:186px;font-size:14px;color:#e8f5fd}
.search{left:177px;top:214px;width:363px;height:45px;display:flex;border-radius:5px;overflow:hidden;box-shadow:0 1px 3px rgba(0,0,0,.3)}
.search input{flex:1;border:0;background:#fff}
.search button{width:53px;border:0;border-left:1px solid #bbb;background:linear-gradient(#f4f4f4,#cfcfcf);display:flex;align-items:center;justify-content:center}
.adv-link{left:176px;top:354px;font-size:19px;color:#fff;display:flex;align-items:center;gap:6px}
.adv-link span{border-bottom:1px dashed #fff;padding-bottom:2px}
.testi-head{left:668px;top:163px;font-family:"Open Sans",Arial,sans-serif;font-size:31px;color:var(--logo-blue)}
.testi-sub{left:669px;top:210px;font-size:14px;color:#e8f5fd}
.testi-source{right:195px;top:252px;font-size:15px;font-weight:700;color:var(--logo-blue)}
.testi-body{left:671px;top:274px;width:336px;font-size:14px;line-height:18px;color:var(--logo-blue)}
.testi-date{right:195px;top:345px;font-size:15px;font-weight:700;color:var(--logo-blue)}
.dots{left:808px;top:394px;display:flex;gap:9px}
.dots i{width:11px;height:11px;border-radius:50%;background:#1a5f92;box-shadow:inset 0 1px 2px rgba(0,0,0,.4)}
.dots i.on{background:#e8eef3}
.badge{left:881px;top:68px}
.band{left:0;top:422px;width:1200px;height:44px;background:linear-gradient(var(--band-top),var(--band-bottom))}
.domains{left:184px;top:433px;width:571px;border-collapse:collapse}
.domains th{font-weight:400;font-size:19px;color:#1d2a1d;height:38px;text-align:left}
.domains td{height:38px;border-bottom:1px solid var(--line);color:var(--green)}
.domains tr.hi td{background:var(--row-hi)}
.domains .dn{font-size:19px;padding-left:8px}
.domains .cat{font-size:15px}
.domains .price{font-size:15px;color:#1d2a1d;text-align:right;padding-right:44px}
.domains .buy{font-size:17px}
.domains tr.hi .buy{font-weight:700}
.all{left:547px;top:710px;font-size:19px;color:#1d2a1d}
.panel{left:786px;top:440px;width:226px;font-size:19px;color:#1d2a1d}
.panel h2{font-weight:400;font-size:23px;margin-bottom:12px}
.panel input[type=text]{border:1px solid #bbb;background:#fff;height:27px}
.panel .kw{width:226px;margin:6px 0 12px}
.checks{display:flex;gap:5px;font-size:18px;margin-top:4px}
.checks label{display:flex;align-items:flex-end;gap:3px}
.checks b{width:15px;height:15px;border:1px solid #999;background:#fff;display:inline-block}
.range{display:flex;align-items:center;margin-top:14px}
.range span.l{width:75px}
.range input{width:57px !important}
.range .to{width:41px;text-align:center}
.divider{left:160px;top:745px;width:900px;height:1px;background:var(--line)}
.photo{left:206px;top:766px;width:101px;height:82px;border:3px solid #fff;box-shadow:0 1px 3px rgba(0,0,0,.3);background:linear-gradient(135deg,#6f8aa0,#c9c2b4 55%,#3e4d5f)}
.q-name{left:322px;top:767px;font-size:19px;color:var(--navy)}
.q-text{left:318px;top:795px;font-size:18px;color:#1a1a1a}
.q-date{left:330px;top:824px;font-size:15px;color:#1a1a1a}
.q-site{right:250px;top:822px;font-size:19px;color:var(--navy)}
.squares{left:583px;top:857px;display:flex;gap:9px}
.squares i{width:11px;height:11px;background:#5a6e80;border:1px solid #5a6e80}
.squares i.off{background:#fff}
.footer{left:0;top:877px;width:1200px;height:84px;background:linear-gradient(90deg,#bdbdbd,#eaeaea 20%,#f2f2f2 50%,#eaeaea 80%,#bdbdbd)}
.addr{left:0;width:1248px;top:893px;text-align:center;font-size:15px;color:var(--footer-text)}
.copy{left:430px;top:927px;font-size:15px;color:var(--footer-text)}
.social{left:829px;top:915px;display:flex;gap:11px}
.social i{width:38px;height:38px;border-radius:50%;background:linear-gradient(#e8e8e8,#c6c6c6);box-shadow:0 1px 3px rgba(0,0,0,.3)}
</style>
</head>
<body>
<header class="abs header">
  <div class="abs logo">ZEPRILO<span style="font-size:14px;letter-spacing:0">.com</span></div>
  <nav class="nav">
    <a class="current" style="left:562px" href="#">Home</a>
    <span class="sep" style="left:621px"></span>
    <a style="left:652px" href="#">Faqs</a>
    <span class="sep" style="left:727px"></span>
    <a style="left:745px" href="#">About Us</a>
    <span class="sep" style="left:843px"></span>
    <a style="left:864px" href="#">Contact</a>
  </nav>
</header>

<section class="abs hero"></section>
<h1 class="abs hero" style="background:none;width:auto;height:auto;left:177px;top:128px;font-size:33px;font-weight:400;color:var(--logo-blue)">Search Your Domain</h1>
<p class="abs" style="left:177px;top:186px;font-size:14px;color:#e8f5fd">You can find the best name for your business...</p>
<form class="abs search">
  <input type="text" aria-label="Domain search">
  <button type="button" aria-label="Search">
    <svg width="22" height="22" viewBox="0 0 22 22"><circle cx="9" cy="9" r="6.5" fill="none" stroke="#333" stroke-width="2.6"/><line x1="14" y1="14" x2="20" y2="20" stroke="#333" stroke-width="3" stroke-linecap="round"/></svg>
  </button>
</form>
<div class="abs adv-link">
  <svg width="20" height="16" viewBox="0 0 20 16"><path d="M1 6h10l-2-3 1-1 5 5v6H6L3 10H1z" fill="none" stroke="#fff" stroke-width="1.4"/></svg>
  <span>Advance Search</span>
</div>

<div class="abs testi-head">Testimonials</div>
<div class="abs testi-sub">what people are saying about us...</div>
<div class="abs testi-source">BRIGHTBOARD.EXAMPLE</div>
<p class="abs testi-body"><b>John:</b>&nbsp; Lorem Ipsum is simply dummy text of the printing and typesetting industry. Lorem Ipsum has been theindustry's standard dummy text ever since the 1500s,</p>
<div class="abs testi-date">May 28, 2013 12:00 am</div>
<div class="abs dots"><i></i><i></i><i></i><i class="on"></i></div>

<svg class="abs badge" width="117" height="114" viewBox="0 0 117 114">
  <defs><linearGradient id="badgeFill" x1="0" y1="0" x2="0" y2="1"><stop offset="0" stop-color="#5cc3f3"/><stop offset="1" stop-color="#1579c0"/></linearGradient></defs>
  <path d="M2 0h113v78L58.5 112 2 78z" fill="#d7eefa"/>
  <path d="M8 0h101v74L58.5 104 8 74z" fill="url(#badgeFill)"/>
  <text x="58.5" y="38" text-anchor="middle" font-family="Arimo,Arial,sans-serif" font-weight="700" font-size="27" fill="#0d3f6e">30%</text>
  <text x="58.5" y="72" text-anchor="middle" font-family="Arimo,Arial,sans-serif" font-weight="700" font-size="27" fill="#0d3f6e">OFF</text>
</svg>

<div class="abs band"></div>
<table class="abs domains">
  <thead><tr><th style="padding-left:44px">Domain</th><th>Category</th><th style="padding-left:16px">Price</th><th>Buy</th></tr></thead>
  <tbody>
    <tr><td class="dn">healvora.example</td><td class="cat">Health</td><td class="price">$8700.00</td><td class="buy">Buy Now</td></tr>
    <tr class="hi"><td class="dn">sportwallets.example</td><td class="cat">Sports</td><td class="price">$5000.00</td><td class="buy">Buy Now</td></tr>
    <tr><td class="dn">cars-vintara.example</td><td class="cat">Vehicals</td><td class="price">$1000.00</td><td class="buy">Buy Now</td></tr>
    <tr><td class="dn">everyhomestead.example</td><td class="cat">Real Estate</td><td class="price">$999.00</td><td class="buy">Buy Now</td></tr>
    <tr><td class="dn">news-q.example</td><td class="cat">Media</td><td class="price">$197.00</td><td class="buy">Buy Now</td></tr>
    <tr><td class="dn">cleardebtpath.example</td><td class="cat">Finance</td><td class="price">$300.00</td><td class="buy">Buy Now</td></tr>
  </tbody>
</table>
<div class="abs all">Search All Domains &#187;</div>

<aside class="abs panel">
  <h2>Advance Search</h2>
  <div>Keywords</div>
  <input class="kw" type="text" aria-label="Keywords">
  <div>Extension</div>
  <div class="checks"><label><b></b>All</label><label><b></b>.com</label><label><b></b>.org</label><label><b></b>.net</label></div>
  <div class="range"><span class="l">Price</span><input type="text" aria-label="Minimum price"><span class="to">To</span><input type="text" aria-label="Maximum price"></div>
  <div class="range"><span class="l">Length</span><input type="text" aria-label="Minimum length"><span class="to">To</span><input type="text" aria-label="Maximum length"></div>
</aside>

<div class="abs divider"></div>
<div class="abs photo" role="img" aria-label="Photo of the customer Selena at her office desk"></div>
<div class="abs q-name">Selena</div>
<div class="abs q-text">“Lorem Ipsum is simply dummy text of the printing and typesetting industry.”</div>
<div class="abs q-date">May 30,2013</div>
<div class="abs q-site">Brightmint.example</div>
<div class="abs squares"><i></i><i class="off"></i><i></i><i></i></div>

<footer class="abs footer"></footer>
<div class="abs addr">Zeprilo, Inc. 1450 Harbor Line Road Suite 210&nbsp; Fairhaven, TN 37000&nbsp; United States +1 555.010.4477</div>
<div class="abs copy">© 2013 Zeprilo, All Right Reserved. Privacy Policy</div>
<div class="abs social" aria-label="Social links"><i></i><i></i><i></i></div>
</body>
</html>
```